We need a very creative business card for a leading diamond tools manufactures in india

1. Iso 9001:2000
2. Logo
3. Leading Manufacture of stone cutting tools: Gang Saw Segment, Circular Segment, wire saw segment and rubber and plastic coated diamond wire rope.
4. Spirit for success
5. Kalvani Mokesh Diamond Tools Pvt. Ltd.
6. Mo. No. 9817406352
7. Email: Rakesh@kmgroup-tardex.com
8. Web: kmgroup-tardex.com
9.CEO
10. Reg. Office. 47, pushpa vihar , naya basti, dholpura ,dist. Rajsamand (rajasthan) 313587
11.Rakesh Jandal
Our audience are Adult based in english speaking person having age between 25-55 that handle granite and marble business.
Plastic

```html
<!DOCTYPE html>
<html lang="en">
<head>
<meta charset="utf-8">
<title>Kalvani Mokesh Diamond Tools – Business Card</title>
<link href="https://fonts.googleapis.com/css2?family=Aldrich&display=swap" rel="stylesheet">
<style>
  :root{
    --stage:#b4bac3;
    --card-light:#ffffff;
    --card-shade:#dcdcdd;
    --brand-red:#b0241f;
    --brand-yellow:#f5c400;
    --ink-grey:#4a4a4a;
    --on-red:#ffffff;
  }
  *{margin:0;padding:0;box-sizing:border-box}
  html,body{width:1200px;height:866px;overflow:hidden}
  body{
    background:var(--stage);
    font-family:"Aldrich",sans-serif;
    position:relative;
  }
  .card{
    position:absolute;
    width:520px;height:300px;
    top:283px;
    background:radial-gradient(ellipse at 45% 40%,var(--card-light) 0%,var(--card-shade) 100%);
    box-shadow:0 6px 18px rgba(0,0,0,.25);
    overflow:hidden;
  }
  .card--front{left:50px}
  .card--back{left:630px}

  .brand{
    display:flex;align-items:center;gap:8px;
    color:var(--brand-red);
    font-size:20px;letter-spacing:.5px;
    white-space:nowrap;
  }
  .brand__dot{
    width:22px;height:22px;border-radius:50%;
    background:var(--brand-yellow);flex:none;
  }
  .card--front .brand{
    position:absolute;left:50%;top:50%;
    transform:translate(-50%,-50%);
  }
  .card--back .brand{
    position:absolute;left:22px;top:118px;
    font-size:15px;gap:6px;
  }
  .card--back .brand__dot{width:16px;height:16px}

  .back-art{position:absolute;inset:0}

  .holder{
    position:absolute;right:22px;top:70px;text-align:right;
  }
  .holder__name{color:var(--brand-red);font-size:17px;letter-spacing:1px}
  .holder__role{color:var(--ink-grey);font-size:12px;margin-top:2px}

  .office{
    position:absolute;right:22px;top:176px;text-align:right;
    color:var(--on-red);font-size:11px;line-height:1.45;
  }
  .web{
    position:absolute;right:22px;top:236px;
    color:var(--on-red);font-size:11px;
  }
  .contacts{
    position:absolute;left:22px;top:236px;
    list-style:none;color:var(--on-red);font-size:10px;
  }
  .contacts li{display:flex;align-items:center;gap:7px;height:14px}
  .contacts svg{width:9px;height:9px;flex:none}
</style>
</head>
<body>

<section class="card card--front" aria-label="Business card front">
  <div class="brand"><span class="brand__dot"></span>Kalvani Mokesh</div>
</section>

<section class="card card--back" aria-label="Business card back">
  <svg class="back-art" viewBox="0 0 520 300" preserveAspectRatio="none" aria-hidden="true">
    <path d="M0,232 C170,205 330,150 520,118 L520,300 L0,300 Z" fill="var(--brand-red)"/>
    <path d="M0,214 C150,186 300,130 430,108 C300,138 160,196 0,228 Z" fill="var(--brand-yellow)"/>
  </svg>

  <div class="brand"><span class="brand__dot"></span>Kalvani Mokesh</div>

  <div class="holder">
    <p class="holder__name">RAKESH JANDAL</p>
    <p class="holder__role">CEO</p>
  </div>

  <p class="office">47, pushpa vihar, naya basti,<br>dholpura, dist. Rajsamand<br>(rajasthan) 313587</p>
  <p class="web">www.kmgroup-tardex.com</p>

  <ul class="contacts">
    <li><svg viewBox="0 0 10 10"><path d="M2,1 L4,1 L4.5,3 L3.5,4 Q4.5,6 6,6.5 L7,5.5 L9,6 L9,8 Q5,9 2,5 Q1,3 2,1Z" fill="currentColor"/></svg>9817406352</li>
    <li><svg viewBox="0 0 10 10"><rect x="2.5" y="0.5" width="5" height="9" rx="1" fill="none" stroke="currentColor"/></svg>9817406352</li>
    <li><svg viewBox="0 0 10 10"><rect x="1" y="4" width="8" height="5" fill="currentColor"/><rect x="3" y="1" width="4" height="3" fill="none" stroke="currentColor"/></svg>9817406352</li>
    <li><svg viewBox="0 0 10 10"><rect x="0.5" y="2" width="9" height="6" fill="currentColor"/><path d="M0.5,2 L5,5.5 L9.5,2" fill="none" stroke="var(--brand-red)"/></svg>Rakesh@kmgroup-tardex.com</li>
  </ul>
</section>

</body>
</html>
```